Business card

I have changed logo's and colors. I have uploaded the new logo and colors.

In my head I am thinking about the main logo and text beside logo to be on one side of the card. The other side of the card to have just my picture and contact information.

The "R" emblem and the "equal housing" emblem... cut he MLS from the "R". and remove the wording from the house emblem.

Info on Card:

Wes Trundell
Designated Broker, CDPE, CNE, GRI
Direct: 602.555.0143
Fax: 623.555.0198
Wes@TrundellandAssociates.example
www.TrundellandAssociates.example
4193 North Sagebend Lane Cactus Flats, AZ 85399

Please see brief as I have uploaded a new logo and a few notes.

Reason: I changed the logo and colors. Please see brief

I am leaning towards maybe a black business card(or at least on the front where the logo is). I liked several designs that were submitted. Please re-submit.

House

```html
<!DOCTYPE html>
<html lang="en">
<head>
<meta charset="utf-8">
<title>Trundell &amp; Associates — Business Card</title>
<link rel="stylesheet" href="https://fonts.googleapis.com/css2?family=Arimo:ital,wght@0,400;0,700;1,400&display=swap">
<style>
  :root {
    --page: #e9e7e4;
    --card-black: #060606;
    --card-charcoal: #222226;
    --accent-orange: #d9782d;
    --accent-slate: #4d6889;
    --text-light: #cfcfcf;
    --badge-grey: #8a8a8a;
    --badge-edge: #bdbdbd;
    --photo-light: #eceae8;
    --photo-dark: #2b2f3a;
  }
  * { box-sizing: border-box; margin: 0; padding: 0; }
  html, body {
    width: 1200px; height: 1146px; overflow: hidden;
    background: var(--page);
    font-family: "Arimo", Arial, sans-serif;
  }
  .sheet { position: relative; width: 1200px; height: 1146px; }
  .card {
    position: absolute; left: 250px;
    width: 700px; height: 400px;
    border-radius: 4px;
    box-shadow: 0 6px 18px rgba(0,0,0,.18);
    overflow: hidden;
  }

  /* Logo side */
  .card--brand { top: 120px; background: var(--card-black); }
  .brand {
    position: absolute; left: 50%; top: 50%;
    transform: translate(-50%, -50%);
    display: flex; align-items: center; gap: 18px;
  }
  .brand__disc {
    flex: none;
    width: 74px; height: 74px; border-radius: 50%;
    background: var(--accent-slate);
  }
  .brand__name {
    color: var(--accent-orange);
    font-weight: 400; font-size: 34px; letter-spacing: 2px;
    line-height: 1.15; white-space: nowrap;
  }

  /* Contact side */
  .card--contact { top: 600px; background: var(--card-charcoal); }
  .contact__name {
    position: absolute; left: 50px; top: 46px;
    color: var(--accent-orange); font-weight: 700; font-size: 42px;
    line-height: 1.1; white-space: nowrap;
  }
  .contact__title {
    position: absolute; left: 52px; top: 98px;
    color: var(--accent-slate); font-style: italic; font-size: 15px;
    white-space: nowrap;
  }
  .contact__lines {
    position: absolute; left: 52px; top: 138px;
    display: grid; grid-template-columns: auto auto; column-gap: 22px;
    color: var(--text-light); font-size: 15px; line-height: 21px;
    white-space: nowrap;
  }
  .contact__web {
    position: absolute; left: 52px; top: 200px;
    color: var(--text-light); font-size: 15px; line-height: 21px;
    white-space: nowrap;
  }
  .badges {
    position: absolute; left: 52px; top: 262px;
    display: flex; gap: 12px; align-items: center;
  }
  .badge { background: var(--badge-grey); border: 2px solid var(--badge-edge); }
  .badge--listing { width: 66px; height: 26px; }
  .badge--housing { width: 32px; height: 32px; background: var(--accent-slate); }
  .portrait {
    position: absolute; left: 440px; top: 90px;
    width: 210px; height: 250px;
    border: 8px solid var(--accent-slate);
    background: linear-gradient(180deg, var(--photo-light) 0%, var(--photo-light) 55%, var(--photo-dark) 100%);
  }
</style>
</head>
<body>
<main class="sheet">
  <section class="card card--brand" aria-label="Card front with company name">
    <div class="brand">
      <span class="brand__disc"></span>
      <span class="brand__name">TRUNDELL &amp;<br>ASSOCIATES</span>
    </div>
  </section>

  <section class="card card--contact" aria-label="Card back with contact details">
    <h1 class="contact__name">Wes Trundell</h1>
    <p class="contact__title">Designated Broker, CDPE, CNE, GRI</p>
    <div class="contact__lines">
      <span>Tele 602.555.0143</span><span>4193 North Sagebend Lane</span>
      <span>Fax 623.555.0198</span><span>Cactus Flats, AZ 85399</span>
    </div>
    <div class="contact__web">
      <p>Wes@TrundellandAssociates.example</p>
      <p>www.TrundellandAssociates.example</p>
    </div>
    <div class="badges">
      <span class="badge badge--listing"></span>
      <span class="badge badge--housing"></span>
    </div>
    <div class="portrait" role="img" aria-label="Portrait photo of the broker in a dark suit"></div>
  </section>
</main>
</body>
</html>
```